Beautiful Simple and Clean WEbsite for Life Coach

Looking for a simple clean site website for life coach for educators. A home page will have an embedded opt-in form, menu bar will be
Work With Me - page for my coaching program and link to online calendar for booking
PRAISE - testimonials
ABOUT
PODCAST
I can supply images and a site I would like it modeled after is https://tessabrook.com/
My current website at www.danawhitfield.com is too dark. I am looking for the white space, pink and magenta. Feel free to use images from the site

Industry/Entity Type

Life Coaching

Number of Pages Required

4 page

Font styles to use
Serif

Colors
E54698
E96AAD
F1A4CE
F9D9EA
FCEFF6

Requirements
Must have
• See attached files for must-haves, Lots of white space, opt-in from for freebie is the most prominent on home page
Nice to have
• refer to Tessa Brook websites
Should not have
• dark colors, any balck background

```html
<!DOCTYPE html>
<html lang="en">
<head>
<meta charset="utf-8">
<title>Lena Marlow – Life Coach for Educators</title>
<link href="https://fonts.googleapis.com/css2?family=Lora:wght@400;500&family=Work+Sans:wght@400;500;600&display=swap" rel="stylesheet">
<style>
:root{
  --magenta:#e54698;
  --pink:#e96aad;
  --pink-mid:#f1a4ce;
  --pink-soft:#f9d9ea;
  --pink-pale:#fcefF6;
  --sage:#d6e1dc;
  --ink:#2b2b2b;
  --text:#555;
  --mauve:#a9848c;
  --white:#fff;
}
*{box-sizing:border-box;margin:0;padding:0}
html,body{width:1200px;height:4600px;overflow:hidden;background:var(--white)}
body{position:relative;font-family:"Work Sans",Arial,sans-serif;color:var(--text);font-size:15px;line-height:1.6}
.abs{position:absolute}
.serif{font-family:"Lora",Georgia,serif;font-weight:400}
.btn{display:inline-block;font-size:11px;letter-spacing:.12em;text-transform:uppercase;padding:12px 26px;font-weight:500}
.btn-pink{background:var(--pink);color:var(--white)}
.btn-outline{border:1px solid var(--pink-mid);color:var(--pink);background:var(--white)}
.photo{background:linear-gradient(160deg,#d9c3bf,#b69a93 55%,#8a6f6c)}

/* header */
.site-header{top:0;left:0;width:1200px;height:80px}
.logo{left:60px;top:20px;font-family:"Lora",Georgia,serif;font-size:30px;color:var(--pink-mid)}
.nav{right:60px;top:26px;display:flex;gap:46px;align-items:center;font-size:12px;letter-spacing:.08em;text-transform:uppercase;color:var(--ink)}
.nav .book{background:var(--sage);padding:9px 24px}

/* hero */
.hero-title{left:130px;top:230px;font-size:50px;line-height:1.15;color:var(--ink)}
.hero-title span{color:var(--pink)}
.hero-list{left:130px;top:370px;font-size:15px;color:var(--ink);line-height:1.9}
.hero .btn{left:130px;top:480px}
.hero-frame{left:618px;top:192px;width:470px;height:420px;border:6px solid var(--pink-soft)}
.hero-photo{left:600px;top:176px;width:460px;height:420px}

/* guide band */
.guide-band{top:560px;left:0;width:1200px;height:620px}
.guide-title{top:770px;left:0;width:1200px;text-align:center;color:var(--white);font-size:38px;line-height:1.2}
.guide-text{top:875px;left:300px;width:600px;text-align:center;color:var(--white);font-size:14px}
.guide .btn{top:950px;left:480px;width:240px;text-align:center}

/* about */
.about-shadow{left:110px;top:1310px;width:410px;height:440px;border-left:6px solid var(--pink-soft);border-bottom:6px solid var(--pink-soft)}
.about-photo{left:126px;top:1290px;width:400px;height:420px}
.about-card{left:505px;top:1350px;width:580px;height:430px;background:var(--white);box-shadow:0 6px 24px rgba(0,0,0,.08);padding:40px 56px}
.about-card::before{content:"";position:absolute;right:-14px;top:-14px;width:100%;height:100%;border-top:6px solid var(--pink-soft);border-right:6px solid var(--pink-soft);z-index:-1}
.about-card h2{font-size:40px;color:var(--ink);line-height:1.1;margin-bottom:16px}
.about-card p{font-size:13px;line-height:1.75;margin-bottom:12px}

/* praise */
.praise-band{top:1840px;left:0;width:1200px;height:720px}
.praise-title{top:1960px;left:0;width:1200px;text-align:center;font-size:40px;color:var(--ink)}
.rule{height:1px;width:64px;background:var(--ink)}
.praise-card{left:265px;top:2100px;width:660px;height:230px;background:var(--white);box-shadow:0 4px 18px rgba(0,0,0,.06);padding:70px 60px 0;text-align:center;font-size:14px}
.praise-avatar{left:562px;top:2062px;width:66px;height:66px;border-radius:50%;border:4px solid var(--white)}
.praise-name{font-weight:600;color:var(--ink);margin-top:18px;font-size:13px}
.praise-role{font-size:12px}
.quote-mark{right:40px;bottom:22px;font-family:"Lora",serif;font-size:70px;color:#ddd;line-height:1}

/* work */
.work-back{left:100px;top:2640px;width:300px;height:440px;background:var(--sage)}
.work-card{left:130px;top:2600px;width:470px;height:450px;background:var(--white);box-shadow:0 6px 24px rgba(0,0,0,.08);padding:56px 56px}
.work-card h2{font-size:40px;color:var(--ink);margin-bottom:14px}
.work-card p{font-size:13px;line-height:1.75;margin-bottom:26px}
.work-photo{left:600px;top:2600px;width:480px;height:450px}

/* podcasts */
.pod-title{top:3180px;left:0;width:1200px;text-align:center;font-size:40px;color:var(--ink)}
.pod{top:3300px;width:350px;height:350px;border-radius:50%;border:4px solid var(--pink-soft);text-align:center;padding:48px 48px 0;background:var(--white)}
.pod.featured{background:var(--pink-mid);border-color:var(--pink-mid);color:var(--white)}
.pod-icon{width:54px;height:54px;border-radius:50%;background:var(--pink-mid);margin:0 auto 18px;display:flex;align-items:center;justify-content:center}
.pod.featured .pod-icon{background:var(--white)}
.pod h3{font-size:15px;font-weight:600;text-transform:uppercase;color:var(--ink);line-height:1.35}
.pod.featured h3{color:var(--white)}
.pod p{font-size:12px;margin:10px 0 14px;line-height:1.5}
.pod .btn{padding:7px 16px;font-size:10px}

/* booking */
.book-band{top:3750px;left:0;width:1200px;height:570px;background:linear-gradient(180deg,var(--pink-pale),var(--pink-soft))}
.book-title{top:3810px;left:0;width:1200px;text-align:center;font-size:36px;color:var(--ink)}
.book-text{top:3880px;left:0;width:1200px;text-align:center;font-size:14px}
.field{background:var(--white);height:44px;width:390px;left:200px;font-size:12px;padding:12px 20px;color:#999;display:flex;gap:10px;align-items:center}
.field svg{flex:none}
.field.msg{left:605px;top:3975px;width:395px;height:164px;align-items:flex-start}
.book .btn{left:490px;top:4160px;width:220px;text-align:center}

/* footer */
.site-footer{top:4320px;left:0;width:1200px;height:280px;background:var(--mauve);color:var(--white)}
.footer-up{left:570px;top:4290px;width:60px;height:60px;border-radius:50%;background:var(--mauve);display:flex;align-items:center;justify-content:center}
.footer-nav{left:140px;top:4385px;display:flex;gap:62px;font-size:11px;letter-spacing:.08em;text-transform:uppercase;color:var(--white)}
.social{right:140px;top:4378px;display:flex;gap:8px}
.social span{width:24px;height:24px;border-radius:50%;background:var(--white)}
.footer-rule{left:140px;top:4420px;width:920px;height:1px;background:rgba(255,255,255,.35)}
.copyright{left:140px;top:4432px;font-size:10px;color:var(--white)}
.legal{right:140px;top:4432px;font-size:10px;display:flex;gap:20px;color:var(--white)}
.disclaimer{left:140px;top:4460px;width:920px;font-size:9px;line-height:1.5;color:var(--white)}
.disclaimer b{display:block}
</style>
</head>
<body>

<header class="site-header abs">
  <div class="logo abs">Lena Marlow</div>
  <nav class="nav abs"><span>Work with me</span><span>Praise</span><span>About</span><span>Podcast</span><span class="book">Book Online</span></nav>
</header>

<section class="hero">
  <h1 class="hero-title serif abs">Life Coach for<br><span>Educators</span></h1>
  <div class="hero-list abs">Being Overworked<br>Being Overwhelmed<br>and not having Work – Life Balance</div>
  <a class="btn btn-pink abs">Learn more about us →</a>
  <div class="hero-frame abs"></div>
  <div class="hero-photo photo abs" role="img" aria-label="Portrait of the coach smiling, wearing a colourful patterned top"></div>
</section>

<section class="guide">
  <svg class="guide-band abs" viewBox="0 0 1200 620" aria-hidden="true">
    <defs><linearGradient id="g" x1="0" y1="0" x2="0" y2="1"><stop offset="0" stop-color="#f1a4ce"/><stop offset="1" stop-color="#f6bcd9"/></linearGradient></defs>
    <polygon points="0,40 1200,0 1200,520 0,600" fill="url(#g)"/>
    <polygon points="0,0 1200,0 1200,60 0,150" fill="#fff" opacity=".55"/>
    <polygon points="0,520 1200,430 1200,620 0,620" fill="#fcefF6"/>
    <polygon points="600,520 1200,430 1200,560" fill="#f9d9ea"/>
    <line x1="600" y1="40" x2="600" y2="175" stroke="#fff" stroke-width="1"/>
    <path d="M594 168 L600 176 L606 168" fill="none" stroke="#fff"/>
  </svg>
  <h2 class="guide-title serif abs">Why School Leaders Need<br>Balance to Succeed</h2>
  <p class="guide-text abs">DISCOVER the secrets on how to prioritize the items on an overwhelming to-do list to get the job done successfully.</p>
  <a class="btn btn-outline abs">Download free guide</a>
</section>

<section class="about">
  <div class="about-shadow abs"></div>
  <div class="about-photo photo abs" role="img" aria-label="Close portrait of the coach in her home office"></div>
  <div class="about-card abs">
    <h2 class="serif">ABOUT ME</h2>
    <p>I'm a Life Coach. I am also a retired Elementary School Principal who loves other educators and everything in education. In my coaching practice, I empower my clients with simple survival skills to succeed at their school and in their life. They have more time, less stress, and yes less.</p>
    <p>If you would like to learn more about how to manage stress and overwhelm, and how to feel better no matter</p>
    <a class="btn btn-outline">Learn more</a>
  </div>
</section>

<section class="praise">
  <svg class="praise-band abs" viewBox="0 0 1200 720" aria-hidden="true">
    <polygon points="0,60 1200,0 1200,600 0,680" fill="#fcefF6"/>
    <polygon points="0,0 260,0 0,70" fill="#d6e1dc" opacity=".8"/>
    <polygon points="700,640 1200,560 1200,720 900,720" fill="#f9d9ea"/>
    <polygon points="1000,660 1200,620 1200,720" fill="#f1a4ce"/>
    <path d="M190 415 L170 430 L190 445 M170 430 H215" fill="none" stroke="#999" stroke-width="2"/>
    <path d="M1010 415 L1030 430 L1010 445 M1030 430 H985" fill="none" stroke="#999" stroke-width="2"/>
  </svg>
  <h2 class="praise-title serif abs">Praise</h2>
  <div class="rule abs" style="left:568px;top:2030px"></div>
  <div class="praise-card abs">
    <p>Lorem ipsum dolor sit amet, consectetur adipiscing elit, sed do eiusmod tempor incididunt ut labore et dolore magna aliqua. Ut enim ad minim veniam, quis nostrud exercitation ullamco laboris nisi</p>
    <div class="praise-name">Carla Dunn</div>
    <div class="praise-role">Weight Coach for Military Moms</div>
    <div class="quote-mark abs">”</div>
  </div>
  <div class="praise-avatar photo abs" role="img" aria-label="Small portrait of the client giving the testimonial"></div>
</section>

<section class="work">
  <div class="work-back abs"></div>
  <div class="work-card abs">
    <h2 class="serif">Work with me</h2>
    <p>I'm a Life Coach. I am also a retired Elementary School Principal who loves other educators and everything in education. In my coaching practice, I empower my clients with simple survival skills to succeed at their</p>
    <a class="btn btn-outline">Learn more →</a>
  </div>
  <div class="work-photo photo abs" role="img" aria-label="The coach outdoors holding a baby in a striped outfit"></div>
</section>

<section class="podcasts">
  <h2 class="pod-title serif abs">Podcasts</h2>
  <div class="rule abs" style="left:568px;top:3245px"></div>
  <article class="pod abs" style="left:60px">
    <div class="pod-icon"><svg width="24" height="24" viewBox="0 0 24 24"><rect x="9" y="3" width="6" height="11" rx="3" fill="#fff"/><path d="M6 11a6 6 0 0 0 12 0M12 17v4" stroke="#fff" stroke-width="1.6" fill="none"/></svg></div>
    <h3>Mother's Day can be filled with conflicting</h3>
    <p>It's Mother's Day weekend, and I am traveling to Texas to see my Mom</p>
    <a class="btn btn-outline">Listen now →</a>
  </article>
  <article class="pod featured abs" style="left:425px">
    <div class="pod-icon"><svg width="24" height="24" viewBox="0 0 24 24"><rect x="9" y="3" width="6" height="11" rx="3" fill="#f1a4ce"/><path d="M6 11a6 6 0 0 0 12 0M12 17v4" stroke="#f1a4ce" stroke-width="1.6" fill="none"/></svg></div>
    <h3>Mother's Day can be filled with conflicting</h3>
    <p>It's Mother's Day weekend, and I am traveling to Texas to see my Mom</p>
    <a class="btn btn-outline">Listen now →</a>
  </article>
  <article class="pod abs" style="left:790px">
    <div class="pod-icon"><svg width="24" height="24" viewBox="0 0 24 24"><rect x="9" y="3" width="6" height="11" rx="3" fill="#fff"/><path d="M6 11a6 6 0 0 0 12 0M12 17v4" stroke="#fff" stroke-width="1.6" fill="none"/></svg></div>
    <h3>Mother's Day can be filled with conflicting</h3>
    <p>It's Mother's Day weekend, and I am traveling to Texas to see my Mom</p>
    <a class="btn btn-outline">Listen now →</a>
  </article>
</section>

<section class="book">
  <div class="book-band abs"></div>
  <h2 class="book-title serif abs">Book an Appointment</h2>
  <div class="rule abs" style="left:568px;top:3866px"></div>
  <p class="book-text abs">DISCOVER the secrets on how to prioritize the items on an overwhelming<br>to-do list to get the job done successfully.</p>
  <div class="field abs" style="top:3975px"><svg width="12" height="12" viewBox="0 0 12 12"><circle cx="6" cy="4" r="2.5" fill="#e96aad"/><path d="M1 12a5 5 0 0 1 10 0z" fill="#e96aad"/></svg>Name</div>
  <div class="field abs" style="top:4035px"><svg width="12" height="12" viewBox="0 0 12 12"><path d="M2 1h3l1 3-1.5 1a6 6 0 0 0 2.5 2.5L8 6l3 1v3a1 1 0 0 1-1 1A9 9 0 0 1 1 2a1 1 0 0 1 1-1z" fill="#e96aad"/></svg>Phone</div>
  <div class="field abs" style="top:4095px"><svg width="12" height="12" viewBox="0 0 12 12"><rect x="1" y="2.5" width="10" height="7" fill="none" stroke="#e96aad"/><path d="M1 3l5 4 5-4" fill="none" stroke="#e96aad"/></svg>Email address</div>
  <div class="field msg abs">Leave a message</div>
  <a class="btn btn-pink abs">Send your message</a>
</section>

<footer class="site-footer abs"></footer>
<div class="footer-up abs"><svg width="16" height="16" viewBox="0 0 16 16"><path d="M3 10 L8 5 L13 10" fill="none" stroke="#fff" stroke-width="1.6"/></svg></div>
<nav class="footer-nav abs"><span>Home</span><span>Work with me</span><span>Praise</span><span>About</span><span>Podcast</span><span>Book online</span></nav>
<div class="social abs"><span></span><span></span><span></span><span></span></div>
<div class="footer-rule abs"></div>
<div class="copyright abs">Copyright © 2023 Lena Marlow. All Right Reserved</div>
<div class="legal abs"><span>Privacy Policy</span><span>Terms Of Use</span></div>
<p class="disclaimer abs"><b>Disclaimer</b>Coaching is not therapy or medical advice. The information shared on this website is for general educational purposes only and does not replace guidance from a licensed professional. Results vary for each client and depend on personal effort and circumstances. By using this site you agree to the terms of use and privacy policy listed above.</p>

</body>
</html>
```